Business cards, envelopes, etc. for real estate company

We have a finished logo for our real estate company. We need a corporate identity package with the following items:

1. Business Cards
2. Letterhead/Stationary - with 2 pages:
-1st page with full header
-2nd page without top header
3. Concise and professional e-mail signature image
4. Fax coversheet
5. Shipping label, with our return address and a mail-to address (on one label)

We need these to be editable. We don't know the industry standard for these items but perhaps you can provide them to us in .PDF and Word format (and if you use Adobe Illustrator for them, .AI as well).

Please use the attached placeholder logo in your design entry. We will provide you with the original logo to swap in (same size and design, just different text) when we choose your entry.

Please include the following information on the letterhead and business cards:

58 West 41st Street
3rd Floor West
New York, NY 10047

Tel: 212-555-0148
Fax :212-555-0148

Please contact us if you have any questions about this contest.
Updates

Hi,

Thanks for your interest in this project. The logo to use should be working now. Please contact me if you have any further issues or questions.

I look forward to seeing your submissions. 

Hi,

We first wish to thank you all for your submissions. 

Here is some general feedback regarding the designs shown:

1. We would prefer square (as opposed to rounded) business cards.

2. For the fax coversheets, we are looking with a designed look. While we understand these are samples, we don't want it to appear as if it a standard block of text or a fax template from a word processing program.

3. For the 1st page of letterhead and envelopes, we do need an office address on them. The envelopes should have space for a stamp in the top right corner. We would prefer the envelopes not to have colored stripes.

4. We think a watermark of the logo is an interesting idea on the business cards and/or letterhead. This may be something to try. However, it is not strictly necessary and we would like to evaluate designs with and without it.

In general we are looking for a clean yet professional look.

We are actively reviewing all entries and thank you for your time and creativity.

One last comment: We understand making all objects in the brief takes some time. However, we want to remind all the designers that this contest is for more than just business cards (envelopes, letterheads, etc.) so if we choose your design, those items will be expected. Please refer to the original brief to see what we are requesting.

If you provide a mockup of any item listed in the brief (in addition to business cards) it would help us visualize your entire vision for this project.

Industry/Entity Type

Real Estate

```html
<!DOCTYPE html>
<html lang="en">
<head>
<meta charset="utf-8">
<title>Hartwell &amp; Hartwell — Business Card</title>
<link rel="stylesheet" href="https://fonts.googleapis.com/css2?family=Source+Sans+3:wght@400;600&display=swap">
<style>
  :root {
    --teal: #2f5866;
    --teal-dark: #22444f;
    --teal-light: #4f7a88;
    --paper: #f4f4f3;
    --ink-grey: #7d7f81;
    --text-grey: #5f6163;
    --rule: #b9bbbc;
    --stage: #e6e6e6;
  }
  * { margin: 0; padding: 0; box-sizing: border-box; }
  html, body {
    width: 1200px; height: 900px; overflow: hidden;
    background: var(--stage);
    font-family: "Source Sans 3", "Myriad Pro", sans-serif;
  }
  .canvas {
    position: relative; width: 1200px; height: 900px;
  }
  .card {
    position: absolute; left: 280px; width: 640px; height: 366px;
    box-shadow: 0 6px 18px rgba(0,0,0,0.18);
    overflow: hidden;
  }
  /* front */
  .card-front {
    top: 70px;
    background: radial-gradient(ellipse at 55% 80%, var(--teal-light) 0%, var(--teal) 55%, var(--teal-dark) 100%);
    display: flex; align-items: center; justify-content: center; gap: 18px;
  }
  .brand-square {
    width: 58px; height: 58px; flex: none;
  }
  .card-front .brand-square { background: #ffffff; }
  .brand-name {
    font-weight: 400; line-height: 0.95; letter-spacing: -0.5px;
  }
  .card-front .brand-name { color: #ffffff; font-size: 34px; }

  /* back */
  .card-back {
    top: 470px;
    background: var(--paper);
  }
  .card-back .bottom-band {
    position: absolute; left: 0; right: 0; bottom: 0; height: 22px;
    background: var(--teal);
  }
  .holder {
    position: absolute; top: 44px; right: 40px; text-align: right;
  }
  .holder-name { color: var(--teal); font-weight: 600; font-size: 19px; line-height: 1.1; }
  .holder-title { color: var(--ink-grey); font-size: 15px; }
  .back-brand {
    position: absolute; left: 40px; top: 108px;
    display: flex; align-items: center; gap: 16px;
  }
  .card-back .brand-square { background: var(--teal); width: 70px; height: 70px; }
  .card-back .brand-name { color: var(--ink-grey); font-size: 38px; }
  .rule-top {
    position: absolute; left: 300px; right: 40px; top: 100px;
    height: 1px; background: var(--rule);
  }
  .rule-contact {
    position: absolute; left: 40px; width: 300px; top: 212px;
    height: 1px; background: var(--rule);
  }
  .contact {
    position: absolute; left: 40px; top: 224px;
    list-style: none; color: var(--text-grey); font-size: 16px; line-height: 1.2;
  }
  .contact li { display: flex; align-items: flex-start; gap: 12px; margin-bottom: 8px; }
  .contact svg { width: 18px; height: 18px; flex: none; margin-top: 1px; }
</style>
</head>
<body>
<main class="canvas">
  <section class="card card-front" aria-label="Business card front">
    <span class="brand-square" aria-hidden="true"></span>
    <span class="brand-name">Hartwell<br>&amp; Hartwell</span>
  </section>

  <section class="card card-back" aria-label="Business card back">
    <div class="holder">
      <p class="holder-name">Alan Brooks</p>
      <p class="holder-title">President</p>
    </div>
    <div class="rule-top"></div>
    <div class="back-brand">
      <span class="brand-square" aria-hidden="true"></span>
      <span class="brand-name">Hartwell<br>&amp; Hartwell</span>
    </div>
    <div class="rule-contact"></div>
    <ul class="contact">
      <li>
        <svg viewBox="0 0 18 18" aria-label="Address"><rect width="18" height="18" fill="#2f5866"/><path d="M9 3.5a3.5 3.5 0 0 0-3.5 3.5c0 2.6 3.5 7 3.5 7s3.5-4.4 3.5-7A3.5 3.5 0 0 0 9 3.5z" fill="#fff"/><circle cx="9" cy="7" r="1.3" fill="#2f5866"/></svg>
        <span>58 West 41st Street, 3rd Floor West<br>New York, NY 10047</span>
      </li>
      <li>
        <svg viewBox="0 0 18 18" aria-label="Telephone"><rect width="18" height="18" fill="#2f5866"/><path d="M4 6.5c0-1.5 2-2.5 5-2.5s5 1 5 2.5v1h-2.5V6.3H6.5v1.2H4z M5.5 9h7l1 4.5h-9z" fill="#fff"/><circle cx="9" cy="11" r="1.2" fill="#2f5866"/></svg>
        <span>212-555-0148</span>
      </li>
      <li>
        <svg viewBox="0 0 18 18" aria-label="Fax"><rect width="18" height="18" fill="#2f5866"/><rect x="6" y="3.5" width="6" height="4" fill="#fff"/><rect x="3.5" y="8" width="11" height="5.5" rx="1" fill="#fff"/><rect x="6" y="11" width="6" height="1.2" fill="#2f5866"/></svg>
        <span>212-555-0148</span>
      </li>
    </ul>
    <div class="bottom-band"></div>
  </section>
</main>
</body>
</html>
```